Promotional Flyer/Email Design - Cabling services for Broadcast and Audio Visual

We need a promotional flyer/email design to help launch our company, Velcor Lane. We provide cabling services for Broadcast Television and Audio Visual systems. Recent projects include major television events such as the Harrowmere Racquet Classic and Audio Visual/Entertainment systems for wealthy clients in their homes and on-board super yachts.

The flyer will be printed as single sided A5 and also be sent out in the body of a promotional email. It should feature the company logo along with a complementary colour scheme. It should have a clean finish with images that show the type of work we do (cabling and equipment installation) or the setting for these systems (tv studio, super yacht, cinema room, meeting room with projector etc.)

Services we offer are:

Broadcast/AV system design
On-site installation
Rack building
Pre-fabricated cable looms
Fibre optic installation

About the company:

Velcor Lane provide cabling services for Broadcast Television and Audio Visual systems. With over 15 years experience working in these industries we can help with every aspect of design, project managment, installation and maintenance. Our projects range from fibre optic cabling at major sports events to installing and commisioning bespoke control systems on some of the worlds largest super yachts.

Contact details:

To get a quote or discuss your project contact us now
Telephone: TBC
Email: info@velcor-lane.com
Website: www.velcor-lane.com
Address: TBC

Other information:

The company is based in London, UK. Our projects often take place in other countries with work taking place accross Europe and beyond.

We have a London based workshop for rack building and cable pre-fabrication.

Our website is www.velcor-lane.com

Images:

Images attached can be editted for use on the flyer or have ideas taken from them. Only the company logo is required to feature on the final design.

Target Market(s)

Business to business

Industry/Entity Type

It Company

Font styles to use
Sans Serif

Requirements
Must have
• Company logo
• List of services
• Contact details
Nice to have
• Image of cabling, home cinema room, super yacht, luxury home, outside broadcast truck, fibre optic equipment or cabling.

```html
<!DOCTYPE html>
<html lang="en">
<head>
<meta charset="utf-8">
<title>Velcor Lane – Cabling Services Flyer</title>
<link href="https://fonts.googleapis.com/css2?family=Source+Sans+3:wght@400;600;700&display=swap" rel="stylesheet">
<style>
  :root {
    --page-bg: #e9e6e1;
    --ink: #2b2b2b;
    --white: #ffffff;
    --brand-red: #e30a47;
    --brand-blue: #1f66c4;
    --brand-blue-deep: #1552a8;
    --brand-purple: #7a2a8c;
    --photo-dark: #3d4148;
    --photo-mid: #6b7079;
  }
  * { box-sizing: border-box; margin: 0; padding: 0; }
  html, body { width: 1200px; height: 1200px; overflow: hidden; background: var(--page-bg); }
  body { font-family: "Source Sans 3", "Myriad Pro", sans-serif; color: var(--ink); }

  .stage { position: relative; width: 1200px; height: 1200px; }
  .flyer {
    position: absolute; left: 600px; top: 600px;
    width: 983px; height: 1375px;
    transform: translate(-50%, -50%) scale(0.8436);
    background: var(--white);
    overflow: hidden;
    box-shadow: 0 6px 24px rgba(0,0,0,0.18);
  }
  .flyer-art { position: absolute; inset: 0; width: 983px; height: 1375px; }

  .brand {
    position: absolute; left: 54px; top: 104px;
    font-size: 40px; font-weight: 600; color: var(--ink);
    display: flex; align-items: center; gap: 12px; letter-spacing: -0.5px;
  }
  .brand-mark { width: 22px; height: 22px; background: var(--brand-red); }

  .intro {
    position: absolute; left: 38px; top: 186px;
    font-size: 21px; line-height: 27px; color: var(--ink);
  }

  .services { position: absolute; left: 42px; top: 390px; }
  .services-title { font-size: 28px; font-weight: 700; margin-bottom: 18px; }
  .services-list { list-style: none; }
  .services-list li {
    display: flex; align-items: center; gap: 10px;
    font-size: 25px; font-weight: 600; height: 40.5px;
  }
  .tick { width: 24px; height: 24px; flex: none; }

  .about {
    position: absolute; right: 37px; top: 910px;
    text-align: right; color: var(--white);
    font-size: 24.5px; line-height: 31px;
  }
  .about p + p { margin-top: 10px; }
  .about .gap { margin-top: 22px; }

  .contact { position: absolute; left: 293px; top: 1208px; color: var(--white); font-size: 24.5px; }
  .contact-lead { margin-bottom: 22px; }
  .contact-row { position: relative; height: 54px; }
  .contact-row span { position: absolute; top: 0; }
  .contact-icon { position: absolute; width: 26px; height: 26px; }
</style>
</head>
<body>
<div class="stage">
  <div class="flyer">
    <svg class="flyer-art" viewBox="0 0 983 1375" xmlns="http://www.w3.org/2000/svg">
      <defs>
        <linearGradient id="stripe" x1="0" y1="0" x2="1" y2="1">
          <stop offset="0" stop-color="#e30a47"/>
          <stop offset="0.5" stop-color="#7a2a8c"/>
          <stop offset="1" stop-color="#2f63cf"/>
        </linearGradient>
        <linearGradient id="rackPhoto" x1="0" y1="0" x2="1" y2="1">
          <stop offset="0" stop-color="#5a5e63"/>
          <stop offset="0.5" stop-color="#3b4350"/>
          <stop offset="1" stop-color="#26292e"/>
        </linearGradient>
        <linearGradient id="blueField" x1="0" y1="0" x2="0" y2="1">
          <stop offset="0" stop-color="#2a72d2"/>
          <stop offset="1" stop-color="#1552a8"/>
        </linearGradient>
        <linearGradient id="lowStripe" x1="0" y1="0" x2="1" y2="0">
          <stop offset="0" stop-color="#e30a47"/>
          <stop offset="0.55" stop-color="#8a2a86"/>
          <stop offset="1" stop-color="#4a4fc4"/>
        </linearGradient>
        <linearGradient id="studioPhoto" x1="0" y1="0" x2="0" y2="1">
          <stop offset="0" stop-color="#3c3d44"/>
          <stop offset="0.55" stop-color="#cfd2d6"/>
          <stop offset="1" stop-color="#b9bcc1"/>
        </linearGradient>
        <linearGradient id="switchPhoto" x1="0" y1="0" x2="1" y2="1">
          <stop offset="0" stop-color="#8d9298"/>
          <stop offset="1" stop-color="#4d5259"/>
        </linearGradient>
        <linearGradient id="cinemaPhoto" x1="0" y1="0" x2="0" y2="1">
          <stop offset="0" stop-color="#b9ac98"/>
          <stop offset="0.6" stop-color="#8b7d6b"/>
          <stop offset="1" stop-color="#5c5148"/>
        </linearGradient>
        <linearGradient id="cablePhoto" x1="0" y1="1" x2="1" y2="0">
          <stop offset="0" stop-color="#6e7075"/>
          <stop offset="0.45" stop-color="#8fa0b4"/>
          <stop offset="0.75" stop-color="#3f6fb0"/>
          <stop offset="1" stop-color="#c27a3e"/>
        </linearGradient>
      </defs>

      <!-- upper right equipment photo -->
      <g role="img" aria-label="Photo of a wired equipment rack with terminal blocks and coloured cables">
        <polygon points="500,0 983,0 983,560" fill="url(#rackPhoto)"/>
      </g>
      <polygon points="480,0 506,0 983,552 983,590" fill="url(#stripe)"/>

      <!-- lower blue field with coloured edge -->
      <polygon points="0,830 983,592 983,612 0,852" fill="url(#lowStripe)"/>
      <polygon points="0,852 983,612 983,1375 0,1375" fill="url(#blueField)"/>
      <polygon points="0,852 983,612 983,625 0,866" fill="#ffffff" opacity="0.85"/>
      <polygon points="0,866 983,625 983,1375 0,1375" fill="url(#blueField)"/>

      <!-- bottom contact band -->
      <path d="M0,1262 C260,1180 600,1150 983,1192 L983,1375 L0,1375 Z" fill="#ffffff"/>
      <path d="M0,1278 C260,1198 600,1168 983,1210 L983,1375 L0,1375 Z" fill="#e30a47"/>

      <!-- cable photo -->
      <g role="img" aria-label="Close-up photo of a stripped multicore power cable">
        <path d="M20,1375 L210,1090 L300,1050 L300,1110 L100,1375 Z" fill="url(#cablePhoto)"/>
      </g>

      <!-- photo circles -->
      <g>
        <circle cx="193" cy="853" r="168" fill="#e30a47"/>
        <circle cx="193" cy="853" r="162" fill="#ffffff"/>
        <circle cx="193" cy="853" r="152" fill="url(#studioPhoto)" role="img" aria-label="Photo of a television studio with a colour-bar backdrop"/>
      </g>
      <g>
        <circle cx="541" cy="743" r="143" fill="#e30a47"/>
        <circle cx="541" cy="743" r="137" fill="#ffffff"/>
        <circle cx="541" cy="743" r="128" fill="url(#switchPhoto)" role="img" aria-label="Photo of a satellite multiswitch with coaxial cables"/>
      </g>
      <g>
        <circle cx="832" cy="660" r="114" fill="#e30a47"/>
        <circle cx="832" cy="660" r="108" fill="#ffffff"/>
        <circle cx="832" cy="660" r="100" fill="url(#cinemaPhoto)" role="img" aria-label="Photo of a home cinema room with projection screen"/>
      </g>
    </svg>

    <div class="brand"><span class="brand-mark"></span>Velcor Lane</div>

    <p class="intro">
      Velcor Lane provide cabling services for Broadcast Television<br>
      and Audio Visual systems. With over 15 years experience<br>
      working in these industries we can help with every aspect of<br>
      design, project managment, installation and maintenance. Our<br>
      projects range from fibre optic cabling at major sports events to<br>
      installing and commisioning bespoke control systems on some<br>
      of the worlds largest super yachts.
    </p>

    <section class="services">
      <h2 class="services-title">Services:</h2>
      <ul class="services-list">
        <li><svg class="tick" viewBox="0 0 24 24"><path d="M3 13 L9 19 L21 5" fill="none" stroke="#e30a47" stroke-width="4" stroke-linecap="round"/></svg>Broadcast/AV system design</li>
        <li><svg class="tick" viewBox="0 0 24 24"><path d="M3 13 L9 19 L21 5" fill="none" stroke="#e30a47" stroke-width="4" stroke-linecap="round"/></svg>On-site installation</li>
        <li><svg class="tick" viewBox="0 0 24 24"><path d="M3 13 L9 19 L21 5" fill="none" stroke="#e30a47" stroke-width="4" stroke-linecap="round"/></svg>Rack building</li>
        <li><svg class="tick" viewBox="0 0 24 24"><path d="M3 13 L9 19 L21 5" fill="none" stroke="#e30a47" stroke-width="4" stroke-linecap="round"/></svg>Pre-fabricated cable looms</li>
        <li><svg class="tick" viewBox="0 0 24 24"><path d="M3 13 L9 19 L21 5" fill="none" stroke="#e30a47" stroke-width="4" stroke-linecap="round"/></svg>Fibre optic installation</li>
      </ul>
    </section>

    <div class="about">
      <p>The company is based in London, UK.</p>
      <p>Our projects often take place in other countries with<br>work taking place accross Europe and beyond.</p>
      <p class="gap">We have a London based workshop for rack building<br>and cable pre-fabrication.</p>
    </div>

    <div class="contact">
      <p class="contact-lead">To get a quote or discuss your project contact us now</p>
      <div class="contact-row">
        <span style="left:0">TBC</span>
        <svg class="contact-icon" style="left:86px;top:2px" viewBox="0 0 24 24"><path d="M7 2 L10 2 L11 7 L8.5 8.5 C9.5 11.5 11.5 14 14.5 15.5 L16 13 L21 14 L21 17 C21 19 19 21 17 21 C9 20 4 14 3.5 6 C3.5 4 5 2 7 2 Z" fill="#ffffff"/></svg>
        <span style="left:290px">info@velcor-lane.com</span>
        <svg class="contact-icon" style="left:600px;top:0" viewBox="0 0 24 24"><rect x="2" y="5" width="20" height="14" fill="#ffffff"/><path d="M2 5 L12 13 L22 5 M2 19 L9 11 M22 19 L15 11" fill="none" stroke="#e30a47" stroke-width="1.6"/></svg>
      </div>
      <div class="contact-row">
        <span style="left:0">TBC</span>
        <svg class="contact-icon" style="left:84px;top:0" viewBox="0 0 24 24"><path d="M12 2 C7.6 2 4.5 5.2 4.5 9.3 C4.5 14.5 12 22 12 22 C12 22 19.5 14.5 19.5 9.3 C19.5 5.2 16.4 2 12 2 Z" fill="#ffffff"/><circle cx="12" cy="9.3" r="3" fill="#e30a47"/></svg>
        <span style="left:290px">www.velcor-lane.com</span>
        <svg class="contact-icon" style="left:600px;top:0;width:30px;height:30px" viewBox="0 0 24 24"><circle cx="12" cy="12" r="10" fill="#ffffff"/><path d="M12 2 V22 M2 12 H22 M12 2 C7 6 7 18 12 22 M12 2 C17 6 17 18 12 22" fill="none" stroke="#e30a47" stroke-width="1.4"/></svg>
      </div>
    </div>
  </div>
</div>
</body>
</html>
```